Hero Image for Homepage Header

I need an hero image (main image) for a new web site.
The site will be a sales consultancy/coaching business aimed at B2B software sales professionals and software/SaaS firms. The aim of the business is to help sales professionals and tech firms transform their sales performance and close more deals.

The two styles of hero images I like can be seen here:
- Plumvane.com
- Dottrick.com

You can come up with a concept that is like one of these.

Basically the image should show a familiar UI screen of a sales professional's CRM dashboard (see attachments).
In the animated gif (which I hate - it's poor quality) you can see how the data points all improve. This represents the sales 'transformation'.

I'd like you to re-create a UI screen from orbelwick.com (the attachments, Orbelwick1 and Orbelwick2 are taken from the Orbelwick CRM software. I want you to recreate them from scratch but in a more high-quality manner and come up with a hero image design concept that will show how poor results on screen can become better.
The attachment Orbelwick2 shows how the results from Orbelwick1 have been improved.

If you think an animated gif would be better, that's fine.

I'd like your design concept to include the following points (in freehand text style just like in the Plumvane.com image)

- 4x pipeline
- Higher conversions
- More deals CLOSED-WON

Come up with something stunning

```html
<!DOCTYPE html>
<html lang="en">
<head>
<meta charset="utf-8">
<title>Sales Transformation Hero</title>
<link rel="stylesheet" href="https://fonts.googleapis.com/css2?family=Open+Sans:wght@300;400;600;700&family=Gochi+Hand&display=swap">
<style>
  :root {
    --ink: #3a3a3a;
    --ink-soft: #555;
    --muted: #8a8a8a;
    --accent: #e89c0c;
    --hand: #e9a21a;
    --peach: #f8e1b3;
    --cta: #fbd24e;
    --cta-line: #f1d26e;
    --cta-text: #f0c453;
    --card-line: #e4e4e4;
    --value: #0e6655;
    --f-blue: #2ea7e0;
    --f-navy: #1d3461;
    --f-aqua: #6fdcd8;
    --f-teal: #14a89a;
    --f-sand: #e5cb7a;
    --f-orange: #f0a30a;
    --g-red: #f2706d;
    --g-yellow: #f8d34b;
    --g-green: #33d197;
  }
  * { box-sizing: border-box; margin: 0; padding: 0; }
  html, body { width: 1200px; height: 675px; overflow: hidden; background: #fff; }
  body { font-family: "Open Sans", Arial, sans-serif; color: var(--ink); }
  .hero { position: relative; width: 1200px; height: 675px; overflow: hidden; background: #fff; }
  .abs { position: absolute; }

  .backdrop { position: absolute; left: 579px; top: -126px; width: 928px; height: 928px; border-radius: 50%; background: var(--peach); }

  .brand { position: absolute; left: 56px; top: 21px; display: flex; align-items: center; gap: 7px; }
  .brand-mark { width: 65px; height: 29px; background: #d9d9d9; }
  .brand-name { font-size: 14px; font-weight: 400; letter-spacing: 3px; color: #222; }

  .nav { position: absolute; top: 19px; left: 955px; display: flex; gap: 17px; }
  .nav a { font-size: 14.5px; font-weight: 600; color: #222; text-decoration: none; }

  .headline { position: absolute; left: 62px; top: 196px; font-weight: 300; font-size: 55px; line-height: 53.5px; color: var(--ink); letter-spacing: -1.2px; }
  .headline .highlight { color: var(--accent); font-weight: 400; }
  .lede { position: absolute; left: 64px; top: 380px; width: 490px; font-size: 12.5px; line-height: 17px; color: var(--ink-soft); }

  .cta { position: absolute; top: 489px; width: 172px; height: 49px; display: flex; align-items: center; justify-content: center; font-size: 16px; letter-spacing: 0.5px; text-decoration: none; }
  .cta-primary { left: 64px; background: var(--cta); color: #fff; }
  .cta-secondary { left: 250px; border: 2px solid var(--cta-line); color: var(--cta-text); background: #fff; }

  .note { position: absolute; font-family: "Gochi Hand", cursive; color: var(--hand); font-size: 22px; line-height: 22px; white-space: nowrap; }
  .arrows { position: absolute; left: 0; top: 0; }

  .dashboard { position: absolute; left: 691px; top: 372px; width: 464px; height: 250px; background: #fff; }
  .dash-bar { position: absolute; left: 3px; top: 5px; width: 300px; height: 19px; background: #d9d9d9; display: flex; align-items: center; gap: 5px; padding-left: 4px; }
  .dash-icon { width: 9px; height: 9px; background: #e0504a; border-radius: 2px; }
  .dash-crumb { font-size: 5.5px; line-height: 5.5px; color: #555; }
  .dash-crumb span { display: block; }
  .dash-crumb .dim { color: #999; }

  .tile { position: absolute; background: #fff; border: 1px solid var(--card-line); border-radius: 6px; overflow: hidden; }
  .tile-title { position: absolute; left: 10px; top: 4px; font-size: 6px; font-weight: 600; color: #444; line-height: 7px; }
  .tile-sub { display: block; font-weight: 400; color: #777; }

  .gauge { position: absolute; }
  .gauge text { font-family: "Open Sans", Arial, sans-serif; }

  .legend { position: absolute; font-size: 4.6px; color: #333; text-align: right; line-height: 7.6px; }
  .legend .legend-head { font-weight: 700; }
  .legend i { display: inline-block; width: 4.5px; height: 4.5px; margin-left: 4px; vertical-align: -0.5px; }
  .sw-blue { background: var(--f-blue); }
  .sw-navy { background: var(--f-navy); }
  .sw-aqua { background: var(--f-aqua); }
  .sw-teal { background: var(--f-teal); }
  .sw-sand { background: var(--f-sand); }
  .sw-orange { background: var(--f-orange); }

  .big-value { position: absolute; left: 18px; top: 33px; font-size: 30px; font-weight: 300; color: var(--value); letter-spacing: -0.5px; }

  .opps { position: absolute; left: 8px; top: 20px; width: 120px; border-collapse: collapse; font-size: 3.6px; }
  .opps th { background: #eee; color: #444; font-weight: 400; height: 12px; text-align: left; padding-left: 4px; }
  .opps th.num { text-align: right; padding-right: 3px; }
  .opps td { height: 5.7px; border-bottom: 0.5px solid #ddd; padding-left: 4px; color: #333; }
  .opps td.name { color: #2a7fd4; }
  .opps td.num { text-align: right; padding-right: 3px; }

  .float-card { position: absolute; background: #fff; box-shadow: 0 2px 6px rgba(0,0,0,0.18); }
  .card-title { position: absolute; left: 15px; top: 14px; font-size: 14px; font-weight: 600; color: #2b2b2b; letter-spacing: 0.3px; }
  .card-sub { position: absolute; left: 15px; top: 35px; font-size: 10px; color: #777; }
  .info { position: absolute; width: 10px; height: 10px; border: 1px solid #666; border-radius: 50%; font-size: 7px; line-height: 8px; text-align: center; color: #666; font-weight: 700; }
  .info-wrap { position: absolute; width: 18px; height: 18px; border-radius: 4px; background: #f1f1f1; }
  .sum-label { position: absolute; left: 22px; top: 7px; font-size: 5.8px; font-weight: 700; color: #222; }
</style>
</head>
<body>
<svg width="0" height="0" style="position:absolute" aria-hidden="true">
  <defs>
    <symbol id="funnel-shape" viewBox="0 0 81 116">
      <polygon points="0,0 81,0 77.63,19.33 3.37,19.33" fill="#2ea7e0"/>
      <polygon points="3.37,19.33 77.63,19.33 74.25,38.67 6.75,38.67" fill="#1d3461"/>
      <polygon points="6.75,38.67 74.25,38.67 70.88,58 10.12,58" fill="#6fdcd8"/>
      <polygon points="10.12,58 70.88,58 67.5,77.33 13.5,77.33" fill="#14a89a"/>
      <polygon points="13.5,77.33 67.5,77.33 64.13,96.67 16.87,96.67" fill="#e5cb7a"/>
      <polygon points="16.87,96.67 64.13,96.67 60.75,116 20.25,116" fill="#f0a30a"/>
    </symbol>
    <symbol id="gauge-arc" viewBox="0 0 200 140">
      <g fill="none" stroke-width="9" stroke-linecap="round">
        <path d="M11.1 128.8 A92 92 0 0 1 20.3 59" stroke="#f2706d"/>
        <path d="M20.3 59 A92 92 0 0 1 146 25.3" stroke="#f8d34b" stroke-linecap="butt"/>
        <path d="M146 25.3 A92 92 0 0 1 188.9 128.8" stroke="#33d197"/>
      </g>
      <g stroke="#555" stroke-width="1">
        <line x1="20" y1="105" x2="24" y2="105"/>
        <line x1="30.7" y1="65" x2="34.2" y2="67"/>
        <line x1="60" y1="35.7" x2="62" y2="39.2"/>
        <line x1="100" y1="25" x2="100" y2="29"/>
        <line x1="140" y1="35.7" x2="138" y2="39.2"/>
        <line x1="169.3" y1="65" x2="165.8" y2="67"/>
        <line x1="180" y1="105" x2="176" y2="105"/>
      </g>
    </symbol>
  </defs>
</svg>

<main class="hero">
  <div class="backdrop"></div>

  <header>
    <div class="brand"><span class="brand-mark"></span><span class="brand-name">LOGO</span></div>
    <nav class="nav"><a href="#">MENU</a><a href="#">LOREM</a><a href="#">CONTACT</a></nav>
  </header>

  <h1 class="headline">Lorem Ipsum Dolor<br><span class="highlight">Lorem Ipsum</span><br>Lorem Ipsum Dolor</h1>
  <p class="lede">Lorem ipsum dolor sit amet, consetetur sadipscing elitr, sed diam nonumy eirmod tempor invidunt ut labore et dolore magna aliquyam erat, sed diam voluptua. At vero eos et accusam et justo duo dolores et ea rebum. Stet clita kasd gubergren, no sea takimata sanctus est Lorem ipsum dolor sit amet. Lorem ipsum dolor sit amet, consetetur sadipscing elitr, sed diam no</p>
  <a class="cta cta-primary" href="#">TRY FOR FREE</a>
  <a class="cta cta-secondary" href="#">GET INFO</a>

  <section class="dashboard">
    <div class="dash-bar"><span class="dash-icon"></span><div class="dash-crumb"><span>Dashboard</span><span>Sales</span><span class="dim">September 2021</span></div></div>

    <div class="tile" style="left:4px;top:36px;width:137px;height:88px;">
      <div class="tile-title">MTD Total ARR<span class="tile-sub">MTD Closed Won Opportunities</span></div>
      <svg class="gauge" style="left:20px;top:20px" width="96" height="67" viewBox="0 0 200 140">
        <use href="#gauge-arc" width="200" height="140"/>
        <polygon points="58,62 104,94 97,102" fill="#1d3461"/>
        <circle cx="100" cy="98" r="4" fill="#1d3461"/>
        <text x="100" y="123" font-size="22" fill="#0e6655" text-anchor="middle" font-weight="600">$ 726 K</text>
        <text x="100" y="139" font-size="15" fill="#666" text-anchor="middle">47%</text>
      </svg>
    </div>

    <div class="tile" style="left:151px;top:36px;width:161px;height:88px;">
      <div class="tile-title">MTD Your Pipeline Opportunities</div>
      <div class="sum-label" style="left:37px;top:17px;font-size:4.6px">Sum of Amount</div>
      <svg class="abs" style="left:36px;top:25px" width="44" height="59" viewBox="0 0 81 116" preserveAspectRatio="none">
        <use href="#funnel-shape" width="81" height="116"/>
        <g fill="#fff" font-size="8" text-anchor="middle" font-family="Open Sans, sans-serif">
          <text x="40.5" y="13">$ 28 K</text><text x="40.5" y="32">$ 56 K</text><text x="40.5" y="52">$ 35 K</text>
          <text x="40.5" y="71">$ 101 K</text><text x="40.5" y="90">$ 158 K</text><text x="40.5" y="110">$ 349 K</text>
        </g>
      </svg>
      <div class="legend" style="right:12px;top:22px;line-height:7.5px">
        <div class="legend-head">Stege</div>
        <div>Initial Contact<i class="sw-blue"></i></div><div>Discovery Call<i class="sw-navy"></i></div>
        <div>Demo Delivered<i class="sw-aqua"></i></div><div>Technical Validation<i class="sw-teal"></i></div>
        <div>Proposal<i class="sw-sand"></i></div><div>Negotiation<i class="sw-orange"></i></div>
      </div>
    </div>

    <div class="tile" style="left:321px;top:36px;width:139px;height:88px;">
      <div class="tile-title" style="top:10px">FYTD Total ARR<span class="tile-sub">FYTD Closed Won Opportunities</span></div>
      <div class="big-value">$1.1 M</div>
    </div>

    <div class="tile" style="left:4px;top:132px;width:137px;height:88px;">
      <div class="tile-title">FYTD Total ARR<span class="tile-sub">FYTD Closed Won Opportunities</span></div>
      <svg class="gauge" style="left:20px;top:19px" width="96" height="67" viewBox="0 0 200 140">
        <use href="#gauge-arc" width="200" height="140"/>
        <polygon points="42,80 102,94 98,103" fill="#1d3461"/>
        <circle cx="100" cy="98" r="4" fill="#1d3461"/>
        <text x="100" y="123" font-size="22" fill="#0e6655" text-anchor="middle" font-weight="600">$ 21 K</text>
        <text x="100" y="139" font-size="15" fill="#666" text-anchor="middle">16%</text>
      </svg>
    </div>

    <div class="tile" style="left:150px;top:132px;width:162px;height:88px;">
      <div class="tile-title">FYTD Your Pipeline Opportunities</div>
      <div class="sum-label" style="left:42px;top:15px;font-size:5.5px">Sum of Amount</div>
      <svg class="abs" style="left:40px;top:22px" width="44" height="59" viewBox="0 0 81 116" preserveAspectRatio="none">
        <use href="#funnel-shape" width="81" height="116"/>
        <g fill="#fff" font-size="8" text-anchor="middle" font-family="Open Sans, sans-serif">
          <text x="40.5" y="13">$ 119 K</text><text x="40.5" y="32">$ 118 K</text><text x="40.5" y="52">$ 228 K</text>
          <text x="40.5" y="71">$ 255 K</text><text x="40.5" y="90">$ 204 K</text><text x="40.5" y="110">$ 88 K</text>
        </g>
      </svg>
      <div class="legend" style="right:13px;top:22px;line-height:7.4px">
        <div class="legend-head" style="font-size:5.5px">Stege</div>
        <div>Initial Contact<i class="sw-blue"></i></div><div>Discovery Call<i class="sw-navy"></i></div>
        <div>Demo Delivered<i class="sw-aqua"></i></div><div>Technical Validation<i class="sw-teal"></i></div>
        <div>Proposal<i class="sw-sand"></i></div><div>Negotiation<i class="sw-orange"></i></div>
      </div>
    </div>

    <div class="tile" style="left:321px;top:132px;width:138px;height:88px;">
      <div class="tile-title" style="left:14px">Your 10 Opportunities<span class="tile-sub" style="margin-left:-2px">FYTD Top 10 FYTD Opportunities</span></div>
      <table class="opps">
        <thead><tr><th>Opportunity Name</th><th class="num"></th><th class="num">ARR</th></tr></thead>
        <tbody>
          <tr><td class="name">Northgate</td><td class="num">69K</td><td class="num">828K</td></tr>
          <tr><td class="name">Kelvra</td><td class="num">53K</td><td class="num">636K</td></tr>
          <tr><td class="name">Arden Trust</td><td class="num">46K</td><td class="num">552K</td></tr>
          <tr><td class="name">Lumio</td><td class="num">38K</td><td class="num">456K</td></tr>
          <tr><td class="name">Harbor Fin</td><td class="num">33K</td><td class="num">396K</td></tr>
          <tr><td class="name">Qarsa Build</td><td class="num">28K</td><td class="num">336K</td></tr>
          <tr><td class="name">Tellix</td><td class="num">28K</td><td class="num">336K</td></tr>
          <tr><td class="name">Brookview Health</td><td class="num">23K</td><td class="num">252K</td></tr>
          <tr><td class="name">Veltro</td><td class="num">18K</td><td class="num">228K</td></tr>
        </tbody>
      </table>
    </div>
  </section>

  <div class="float-card" style="left:783px;top:125px;width:197px;height:51px;">
    <div class="card-title" style="top:14px">PIPELINE</div>
    <div class="card-sub" style="top:36px">September 2021</div>
    <div class="info-wrap" style="left:163px;top:16px"><span class="info" style="left:4px;top:4px">i</span></div>
  </div>
  <div class="float-card" style="left:783px;top:181px;width:197px;height:152px;">
    <div class="sum-label">Sum of Amount</div>
    <svg class="abs" style="left:11px;top:20px" width="81" height="116" viewBox="0 0 81 116">
      <use href="#funnel-shape" width="81" height="116"/>
      <g fill="#fff" font-size="7" text-anchor="middle" font-family="Open Sans, sans-serif">
        <text x="40.5" y="12">$ 28 K</text><text x="40.5" y="31.5">$ 56 K</text><text x="40.5" y="51">$ 35 K</text>
        <text x="40.5" y="70">$ 101 K</text><text x="40.5" y="89.5">$ 158 K</text><text x="40.5" y="109">$ 349 K</text>
      </g>
    </svg>
    <div class="legend" style="right:17px;top:16px;font-size:6px;line-height:14.7px">
      <div class="legend-head">Stege</div>
      <div>Initial Contact<i class="sw-blue" style="width:8px;height:8px;margin-left:9px"></i></div>
      <div>Discovery Call<i class="sw-navy" style="width:8px;height:8px;margin-left:9px"></i></div>
      <div>Demo Delivered<i class="sw-aqua" style="width:8px;height:8px;margin-left:9px"></i></div>
      <div>Technical Validation<i class="sw-teal" style="width:8px;height:8px;margin-left:9px"></i></div>
      <div>Proposal<i class="sw-sand" style="width:8px;height:8px;margin-left:9px"></i></div>
      <div>Negotiation<i class="sw-orange" style="width:8px;height:8px;margin-left:9px"></i></div>
    </div>
  </div>

  <div class="float-card" style="left:995px;top:227px;width:189px;height:191px;">
    <div class="card-title" style="top:15px">FYTD Total ARR</div>
    <div class="card-sub" style="left:15px;top:37px">FYTD Closed Won Opportunities</div>
    <div style="position:absolute;left:0;top:48px;width:189px;height:1px;background:#ddd"></div>
    <div class="info-wrap" style="left:154px;top:16px"><span class="info" style="left:4px;top:4px">i</span></div>
    <svg class="gauge" style="left:8px;top:55px" width="178" height="125" viewBox="0 0 200 140">
      <use href="#gauge-arc" width="200" height="140"/>
      <polygon points="94,22 106,82 98,84" fill="#1d3461"/>
      <text x="100" y="111" font-size="25" fill="#0e6655" text-anchor="middle" font-weight="600">$ 726 K</text>
      <text x="100" y="131" font-size="18" fill="#555" text-anchor="middle">47%</text>
    </svg>
  </div>

  <div class="note" style="left:784px;top:75px">4x pipeline</div>
  <div class="note" style="left:1056px;top:110px;line-height:22px">Closed-won<br>More Deals</div>
  <div class="note" style="left:664px;top:285px;line-height:22px;text-align:center">Higher<br>conversions</div>
  <svg class="arrows" width="1200" height="675" viewBox="0 0 1200 675" fill="none" stroke="#e9a21a" stroke-width="3" stroke-linecap="round" stroke-linejoin="round" aria-hidden="true">
    <path d="M822 70 C 855 42, 930 48, 925 120"/>
    <polyline points="915,107 925,122 933,106"/>
    <path d="M1073 137 C 1028 152, 1015 195, 1043 222"/>
    <polyline points="1029,214 1043,223 1045,207"/>
    <path d="M762 304 C 805 295, 830 330, 822 370"/>
    <polyline points="812,357 822,371 831,357"/>
  </svg>
</main>
</body>
</html>
```